A website design for a consultation firm

We are located in Istanbul, Turkey and offers our consultation services to customers interested in investing in Realestate, Education and Investment particularly this coming from Arab world and English speaking countries.

The site should carry our message of deep knowledge about the Turkish markets in the mentioned sectors of interest, sincerity and keenness.

The final deliverable of the winning design should include:
- The source files of the final designs. e.g. AI, PSD ..etc
- The redline markup for the design using a Specctr or any other similar tool.

Target Market(s)

English and Arabic speaking countries with a Turkish theme since we are a Turkish company

Industry/Entity Type

Consulting

Number of Pages Required

2 page

Font styles to use
Sans Serif

Requirements
Must have
• The site should serve the following main sections:
• - Why QVE?
• - Reports & studies
• - Sectors
• - Our team
• - Contact
• We need a design that could be converted into a WordPress theme.
• The design should be in English but should accommodate other languages including RTL.
• You can use the color theme you like as long as it does't dissolve the logo.
• The site should link into our accounts on the following networks:
• - Twitter
• - Facebook
• - LinkedIn
• The design should be responsive and nicely rendered on Desktop, Tablets and Smart phones.
Nice to have
• The site would be nice to balance between being informative and

```html
<!DOCTYPE html>
<html lang="en">
<head>
<meta charset="utf-8">
<title>QVE Consulting</title>
<link href="https://fonts.googleapis.com/css2?family=Exo+2:wght@600;700&family=Lato:wght@400;700&display=swap" rel="stylesheet">
<style>
:root{
  --red:#e2161f;
  --navy:#1d2f6b;
  --ink:#222;
  --text:#333;
  --soft:#f2f2f2;
  --line:#cfcfcf;
  --dark:#333335;
  --white:#fff;
  --leaf-light:#e3f1c2;
  --leaf:#a9d256;
}
*{box-sizing:border-box;margin:0;padding:0}
html,body{width:746px;height:1200px;overflow:hidden}
body{position:relative;font-family:"Lato",sans-serif;color:var(--text);background:var(--white)}
.abs{position:absolute}
.title{font-family:"Exo 2",sans-serif;font-weight:700;text-align:center;font-size:23px;letter-spacing:.2px;white-space:nowrap}
.title .r{color:var(--red)}
.title .n{color:var(--navy)}
.divider{height:1px;background:var(--line)}

/* header */
.site-header{left:0;top:0;width:746px;height:85px;background:var(--white)}
.brand{left:62px;top:20px;display:flex;align-items:center;gap:6px}
.brand-dot{width:16px;height:16px;border-radius:50%;background:var(--red)}
.brand-name{font-weight:700;font-size:22px;color:var(--navy);line-height:1}
.contact-top{top:19px;display:flex;align-items:center;gap:5px;font-size:7.5px;color:var(--ink)}
.contact-top svg{width:14px;height:14px}
.lang{left:661px;top:19px;display:flex;align-items:center;gap:5px}
.lang .flag{width:13px;height:13px;border-radius:50%;background:#2c3e8c;border:1px solid #ccc}
.main-nav{top:55px;left:235px;font-size:10.5px;color:var(--ink)}
.main-nav a{color:inherit;text-decoration:none;position:absolute;white-space:nowrap}
.main-nav .active{color:var(--red)}
.nav-underline{left:231px;top:71px;width:36px;height:2px;background:var(--red)}

/* hero */
.hero{left:0;top:85px;width:746px;height:320px;
  background:linear-gradient(90deg,var(--leaf-light) 0%,var(--leaf) 40%,#c9e38f 62%,#e8ddd0 80%,#2a3040 100%)}
.hero-copy{left:58px;top:188px;width:250px;text-align:center;font-weight:700;font-size:19.5px;line-height:25.5px;color:#1b1b1b;white-space:nowrap}
.cta{left:121px;top:294px;width:120px;height:26px;border-radius:13px;background:var(--red);color:var(--white);
  font-weight:700;font-size:12px;display:flex;align-items:center;padding-left:11px;gap:7px}
.cta .arrow{width:18px;height:18px;border-radius:50%;background:var(--white);display:flex;align-items:center;justify-content:center}

/* welcome */
.welcome{left:0;top:405px;width:746px;height:189px;background:var(--soft)}
.welcome p{left:63px;top:77px;width:620px;text-align:center;font-size:9.8px;line-height:15.3px;color:var(--ink)}
.read-more{left:0;width:746px;top:151px;text-align:center;font-size:9.5px;color:var(--ink);text-decoration:underline}

/* sectors */
.sector{width:190px;text-align:center}
.sector .icon{width:68px;height:68px;border-radius:50%;margin:0 auto;background:radial-gradient(circle at 40% 35%,#f23a40,#c4121a);display:flex;align-items:center;justify-content:center;box-shadow:0 10px 8px -8px rgba(0,0,0,.18)}
.sector h3{font-family:"Exo 2",sans-serif;font-weight:700;font-size:14px;color:var(--navy);margin-top:24px;letter-spacing:.3px}
.sector p{font-size:8.4px;line-height:13px;color:var(--ink);margin-top:8px}

/* why / testimonials */
.lower{left:0;top:858px;width:746px;height:231px;background:var(--soft)}
.why-intro{left:62px;top:75px;width:290px;font-size:8.4px;line-height:13.5px;color:var(--ink)}
.why-list{left:62px;top:124px;list-style:none;font-size:8.4px;color:var(--ink)}
.why-list li{display:flex;align-items:center;gap:8px;height:18px}
.why-list .tick{width:9px;height:9px;border-radius:50%;background:var(--red);display:flex;align-items:center;justify-content:center}
.faint-brand{left:250px;top:152px;font-weight:700;font-size:18px;color:rgba(170,170,170,.3);white-space:nowrap}
.quote-box{left:395px;top:76px;width:289px;height:86px;background:var(--white);border-radius:4px;box-shadow:0 0 4px rgba(0,0,0,.08);padding:10px 12px 0 12px;text-indent:22px;font-size:8.3px;line-height:13.6px;color:var(--ink)}
.quote-mark{left:405px;top:82px;font-family:Georgia,serif;font-size:26px;color:#bbb;line-height:1}
.avatar{left:406px;top:1019px;width:44px;height:44px;border-radius:50%;background:linear-gradient(135deg,#9aa7b5,#5b6472);border:2px solid var(--white)}
.client-name{left:538px;top:1034px;font-size:9px;font-weight:700;color:var(--navy)}

/* footer */
.footer-nav{left:0;top:1089px;width:746px;height:42px;background:var(--red)}
.footer-nav ul{position:absolute;left:62px;top:15px;display:flex;list-style:none;font-size:8.4px;font-weight:700;color:var(--white)}
.footer-nav li+li::before{content:"|";margin:0 8px;font-weight:400}
.social{top:12px;width:19px;height:19px;border-radius:50%;background:var(--white)}
.footer-info{left:0;top:1131px;width:746px;height:69px;background:var(--dark);color:var(--white)}
.info-item{top:22px;display:flex;gap:9px;align-items:flex-start}
.info-item .ic{width:19px;height:19px;border-radius:50%;background:var(--white);display:flex;align-items:center;justify-content:center;margin-top:3px}
.info-item strong{display:block;font-size:9.5px;margin-bottom:4px}
.info-item span{font-size:7.8px;color:#e8e8e8}
.copyright{left:540px;top:26px;width:144px;text-align:right;font-size:7.8px;line-height:12.5px;color:#e8e8e8}
</style>
</head>
<body>

<header class="site-header abs">
  <div class="brand abs"><span class="brand-dot"></span><span class="brand-name">qve consulting</span></div>
  <div class="contact-top abs" style="left:446px">
    <svg viewBox="0 0 16 16"><circle cx="8" cy="8" r="7" fill="none" stroke="#e2161f" stroke-width="1.2"/><path d="M5.5 4.5l1.5 0 .6 2-1 .8a5 5 0 0 0 2.1 2.1l.8-1 2 .6v1.5c0 .5-.5.8-1 .8A6 6 0 0 1 4.7 5.5c0-.5.3-1 .8-1z" fill="#e2161f"/></svg>
    123 456 7890
  </div>
  <div class="contact-top abs" style="left:531px">
    <svg viewBox="0 0 16 16"><circle cx="8" cy="8" r="7" fill="none" stroke="#e2161f" stroke-width="1.2"/><rect x="4.5" y="5.5" width="7" height="5" fill="#e2161f"/><path d="M4.5 5.5l3.5 3 3.5-3" stroke="#fff" stroke-width=".8" fill="none"/></svg>
    inquiry@qveconsulting.com
  </div>
  <div class="lang abs"><span class="flag"></span><svg width="7" height="5" viewBox="0 0 7 5"><path d="M0 0h7L3.5 5z" fill="#222"/></svg></div>
  <nav class="main-nav abs">
    <a class="active" style="left:1px">Home</a>
    <a style="left:53px">Why Choose Us?</a>
    <a style="left:156px">Reports &amp; Studies</a>
    <a style="left:265px">Sectors</a>
    <a style="left:324px">Our Team</a>
    <a style="left:396px">Contact Us</a>
  </nav>
  <div class="nav-underline abs"></div>
</header>

<section class="hero abs" role="img" aria-label="Photo of cupped hands holding coins with a green sapling growing from them, on a soft green background"></section>
<h1 class="hero-copy abs">Looking To Minimize The<br>New Market Entrance Risk?<br>Your Search Is Over</h1>
<a class="cta abs">GET STARTED <span class="arrow"><svg width="8" height="8" viewBox="0 0 8 8"><path d="M2.5 1l3 3-3 3" stroke="#222" stroke-width="1.6" fill="none"/></svg></span></a>

<section class="welcome abs">
  <h2 class="title abs" style="left:0;width:746px;top:24px"><span class="r">welcome to</span> <span class="n">qve consulting</span></h2>
  <div class="divider abs" style="left:289px;top:64px;width:169px"></div>
  <p class="abs">Sed ut perspiciatis unde omnis iste natus error sit voluptatem accusantium dolo remque laudantium, totam rem aperiam, eaque ipsa quae ab illo inventore veritatis et quasi architecto beatae vitae dicta sunt explicabo. Sed ut perspiciatis unde omnis iste natus error sit voluptatem accusantium dolo. Sed ut perspiciatis unde omnis iste natus error sit voluptatem accusantium dolo.Sed ut perspiciatis unde omnis iste natus error sit voluptatem accusantium dolo.</p>
  <a class="read-more abs">Read More+</a>
</section>

<section class="sectors">
  <h2 class="title abs" style="left:0;width:746px;top:621px"><span class="r">sectors we</span> <span class="n">work with</span></h2>
  <div class="divider abs" style="left:289px;top:660px;width:169px"></div>

  <div class="sector abs" style="left:73px;top:678px">
    <div class="icon"><svg width="36" height="32" viewBox="0 0 36 32"><path d="M18 2L2 16h5v14h8v-9h6v9h8V16h5z" fill="#fff"/></svg></div>
    <h3>Real estate</h3>
    <p>Lorem ipsum dolor sit amet,<br>consectetuer adipiscing elit, sed diam<br>nonummy nibh euismod tincid</p>
  </div>
  <div class="sector abs" style="left:278px;top:678px">
    <div class="icon"><svg width="40" height="34" viewBox="0 0 40 34"><path d="M20 4L2 12l18 8 18-8z" fill="#fff"/><path d="M9 16v8c0 3 5 6 11 6s11-3 11-6v-8l-11 5z" fill="none" stroke="#fff" stroke-width="2"/><path d="M6 14v12" stroke="#fff" stroke-width="1.6"/><circle cx="6" cy="27" r="1.8" fill="#fff"/></svg></div>
    <h3>Education</h3>
    <p>Lorem ipsum dolor sit amet,<br>consectetuer adipiscing elit, sed diam<br>nonummy nibh euismod tincid</p>
  </div>
  <div class="sector abs" style="left:477px;top:678px">
    <div class="icon"><svg width="38" height="34" viewBox="0 0 38 34"><rect x="11" y="3" width="18" height="14" rx="1.5" fill="none" stroke="#fff" stroke-width="2"/><circle cx="20" cy="10" r="3" fill="#fff"/><path d="M3 24l8-3h9c2 0 2 3 0 3h-6M20 24l10-5c2-1 4 1 2 3l-10 7H8l-5 2" fill="none" stroke="#fff" stroke-width="2" stroke-linejoin="round"/></svg></div>
    <h3>Investments</h3>
    <p>Lorem ipsum dolor sit amet,<br>consectetuer adipiscing elit, sed diam<br>nonummy nibh euismod tincid</p>
  </div>
</section>

<section class="lower abs">
  <h2 class="title abs" style="left:62px;top:26px;text-align:left"><span class="r">why</span> <span class="n">choose us</span></h2>
  <div class="divider abs" style="left:62px;top:62px;width:289px"></div>
  <p class="why-intro abs">Loren &nbsp;autem vel eum iriure hendrerit in vulputate velit esse molestie. ererer onsectetuer adipiscing elit, sed diam nonummy nibh euismod tincidunt u euer feugiat nulla facilisis awerjeowrjewopr</p>
  <ul class="why-list abs">
    <li><span class="tick"><svg width="6" height="5" viewBox="0 0 6 5"><path d="M.5 2.5l1.7 1.6L5.5.8" stroke="#fff" stroke-width="1.2" fill="none"/></svg></span>Autem vel eum iriure hendrerit in</li>
    <li><span class="tick"><svg width="6" height="5" viewBox="0 0 6 5"><path d="M.5 2.5l1.7 1.6L5.5.8" stroke="#fff" stroke-width="1.2" fill="none"/></svg></span>Gendrerit in vulputate velit</li>
    <li><span class="tick"><svg width="6" height="5" viewBox="0 0 6 5"><path d="M.5 2.5l1.7 1.6L5.5.8" stroke="#fff" stroke-width="1.2" fill="none"/></svg></span>Autem vel eum adipiscing elit, sed diam</li>
    <li><span class="tick"><svg width="6" height="5" viewBox="0 0 6 5"><path d="M.5 2.5l1.7 1.6L5.5.8" stroke="#fff" stroke-width="1.2" fill="none"/></svg></span>Eeum iriure hendrerit in vulputate velit</li>
    <li><span class="tick"><svg width="6" height="5" viewBox="0 0 6 5"><path d="M.5 2.5l1.7 1.6L5.5.8" stroke="#fff" stroke-width="1.2" fill="none"/></svg></span>Eeum iriure hendrerit in vulputate velit</li>
  </ul>
  <div class="faint-brand abs">qve consulting</div>

  <h2 class="title abs" style="left:395px;top:26px;text-align:left"><span class="r">client</span> <span class="n">testimonials</span></h2>
  <div class="divider abs" style="left:395px;top:62px;width:289px"></div>
  <blockquote class="quote-box abs">Lorem ipsum dolor sit amet consetug e sed diay nibh uismodl erer ewrerer tincidunt ut laoreet dolore magam er vol wisi enim ad minimer eniam quisere nostrud exerci tationorem ipsum dolor sit ametee seder iammy nibh werwe euismd tincidunt ut laoreet dolore magna aliqurwi volpatl iidunt ut laoreeter dolore magna aliqurr sit ametee.</blockquote>
  <div class="quote-mark abs">&ldquo;</div>
</section>
<div class="avatar abs" role="img" aria-label="Portrait photo of the client"></div>
<div class="client-name abs">Mr Adam Kerr</div>

<footer>
  <nav class="footer-nav abs">
    <ul><li>Home</li><li>Why Choose Us?</li><li>Reports &amp; Studies</li><li>Sectors</li><li>Our Team</li><li>Contact Us</li></ul>
    <span class="social abs" style="left:611px" aria-label="Facebook"></span>
    <span class="social abs" style="left:638px" aria-label="Twitter"></span>
    <span class="social abs" style="left:665px" aria-label="YouTube"></span>
  </nav>
  <div class="footer-info abs">
    <div class="info-item abs" style="left:62px">
      <span class="ic"><svg width="9" height="11" viewBox="0 0 9 11"><path d="M4.5 0A4 4 0 0 0 .5 4c0 3 4 7 4 7s4-4 4-7a4 4 0 0 0-4-4z" fill="#333"/><circle cx="4.5" cy="4" r="1.5" fill="#fff"/></svg></span>
      <div><strong>qve consulting</strong><span>123, Lorewam Dollar, Smit Amet dollar</span></div>
    </div>
    <div class="info-item abs" style="left:257px">
      <span class="ic"><svg width="10" height="10" viewBox="0 0 10 10"><path d="M1.5 1h2l.8 2.3-1.2 1a6 6 0 0 0 2.6 2.6l1-1.2 2.3.8v2c0 .6-.5 1-1 1A8 8 0 0 1 .5 2c0-.5.4-1 1-1z" fill="#333"/></svg></span>
      <div><strong>Call Us</strong><span>123 456 7890</span></div>
    </div>
    <div class="info-item abs" style="left:369px">
      <span class="ic"><svg width="10" height="8" viewBox="0 0 10 8"><rect width="10" height="8" fill="#333"/><path d="M0 0l5 4 5-4" stroke="#fff" stroke-width="1" fill="none"/></svg></span>
      <div><strong>Email Us</strong><span>info@qveconsulting.com</span></div>
    </div>
    <div class="copyright abs">Copyright &copy; 2016 QVE Consulting.<br>All Rights Reserved.</div>
  </div>
</footer>

</body>
</html>
```